RP-Steuerberatung WordPress Site fully implemented (tax advisor)

Hello!
I need a little Wordpress Site for my newly founded Tax-Advisor Company.
I am a one-man Office advising in the area of Crypto-Currency.
PLEASE only provide a Design, if you can also Implement a WP-Site afterwards on an existing Webspace.

Please find the Content and Website-Description in the attached Document

Language for the Website is German (for now)

Target Market(s)

Tax-Advisory (specialized in Crypto Currency)

Coding

Coded - Design and coding required

Number of Pages Required

5+ page

Font styles to use
Sans Serif

Requirements
Must have
• Wordpress Implementation afterwards - Details according to attached Project Information Document

```html
<!DOCTYPE html>
<html lang="de">
<head>
<meta charset="utf-8">
<title>RP-Steuerberatung</title>
<link href="https://fonts.googleapis.com/css2?family=Inter:wght@400;500;600;700&display=swap" rel="stylesheet">
<style>
:root{
  --navy:#1c2a40;
  --ink:#111318;
  --white:#ffffff;
  --accent:#1d3f8f;
  --footer:#272b36;
  --rule:#2a2d33;
}
*{margin:0;padding:0;box-sizing:border-box}
html,body{width:760px;height:1200px;overflow:hidden;background:var(--white)}
body{font-family:"Inter",sans-serif;color:var(--ink);position:relative}
.topbar{position:absolute;left:0;top:0;width:760px;height:23px;background:var(--navy);color:#dfe3ea;font-size:6.5px}
.social{position:absolute;top:7px;width:10px;height:10px;border:1.3px solid #fff;border-radius:2px}
.topbar .contact{position:absolute;top:7px;display:flex;align-items:center;gap:4px}
.header{position:absolute;left:0;top:23px;width:760px;height:65px;background:var(--white)}
.brand{position:absolute;display:flex;align-items:center;gap:8px;font-weight:700;letter-spacing:.3px}
.brand .mark{width:18px;height:18px;background:currentColor}
.header .brand{left:66px;top:23px;font-size:13px;color:var(--navy)}
.nav{position:absolute;top:26px;font-size:9.6px;font-weight:500;color:var(--ink)}
.nav.active{color:var(--accent)}
.nav.active::after{content:"";position:absolute;left:0;right:0;bottom:-5px;height:1.2px;background:var(--accent)}
.hero{position:absolute;left:0;top:88px;width:760px;height:318px;overflow:hidden;
  background:linear-gradient(180deg,#170d33 0%,#1b2a7a 45%,#1540b8 78%,#0c3ab8 100%)}
.hero h1{position:absolute;left:0;right:0;top:112px;text-align:center;color:var(--white);font-size:38px;font-weight:600;line-height:45px;letter-spacing:.2px}
.arrow-btn{position:absolute;width:34px;height:34px;border-radius:50%;background:#eceef2;display:flex;align-items:center;justify-content:center}
.hero svg.band{position:absolute;left:0;bottom:0}
.feature-image{position:absolute;left:80px;top:437px;width:267px;height:267px;border-radius:6px;
  background:radial-gradient(circle at 65% 55%,#1aa6c8 0%,#0c4d8e 35%,#0d2352 70%,#0a1630 100%)}
.intro{position:absolute;left:390px;top:475px;width:300px;font-size:19.3px;line-height:23px;font-weight:400}
.cta{position:absolute;left:395px;top:590px;width:180px;height:31px;border-radius:4px;background:var(--navy);color:var(--white);
  font-size:9.6px;font-weight:500;display:flex;align-items:center;justify-content:center;gap:8px}
.section-title{position:absolute;left:0;right:0;top:753px;text-align:center;font-size:19px;font-weight:600}
.quote{position:absolute;left:164px;width:432px;height:80px;border-bottom:1px solid var(--rule)}
.quote .num{position:absolute;left:4px;top:19px;width:40px;height:40px;border:1px solid var(--rule);border-radius:50%;
  display:flex;align-items:center;justify-content:center;font-size:18px;font-weight:600;color:var(--navy)}
.quote p{position:absolute;left:61px;top:23px;width:340px;font-size:12.6px;line-height:15.5px;font-weight:500;color:#1a1d24}
.footer{position:absolute;left:0;top:1092px;width:760px;height:108px;background:var(--footer);color:var(--white)}
.footer .brand{left:73px;top:31px;font-size:11.5px;color:var(--white)}
.footer .brand .mark{width:15px;height:15px}
.footer .contact{position:absolute;left:258px;top:35px;font-size:8.3px;line-height:10px;font-weight:500}
.footer .fnav{position:absolute;top:44px;font-size:8.2px;font-weight:500}
.footer .rule{position:absolute;left:67px;top:75px;width:627px;height:1px;background:#c9ccd3}
.footer .copy{position:absolute;left:0;right:0;top:86px;text-align:center;font-size:6.5px;font-weight:500}
</style>
</head>
<body>
<div class="topbar">
  <span class="social" style="left:68px"></span>
  <span class="social" style="left:88px;border-radius:50%"></span>
  <span class="contact" style="left:524px">
    <svg width="8" height="8" viewBox="0 0 24 24"><path fill="#fff" d="M6.6 10.8a15 15 0 0 0 6.6 6.6l2.2-2.2c.3-.3.7-.4 1-.2 1.1.4 2.3.6 3.6.6.6 0 1 .4 1 1V20c0 .6-.4 1-1 1A17 17 0 0 1 3 4c0-.6.4-1 1-1h3.5c.6 0 1 .4 1 1 0 1.3.2 2.5.6 3.6.1.3 0 .7-.2 1z"/></svg>
    +43 512 480 276
  </span>
  <span class="contact" style="left:608px">
    <svg width="10" height="8" viewBox="0 0 20 14"><rect width="20" height="14" rx="1.5" fill="#fff"/><path d="M1 1l9 7 9-7" fill="none" stroke="#1c2a40" stroke-width="1.6"/></svg>
    &nbsp;office@rp-steuer.example
  </span>
</div>

<header class="header">
  <div class="brand"><span class="mark"></span>RP STEUERBERATUNG</div>
  <span class="nav active" style="left:391px">HOME</span>
  <span class="nav" style="left:434px">LEISTUNGEN</span>
  <span class="nav" style="left:509px">ÜBER MICH</span>
  <span class="nav" style="left:574px">KONTAKT</span>
  <span class="nav" style="left:634px">IMPRESSUM</span>
</header>

<section class="hero" role="img" aria-label="Dunkelblauer Hintergrund mit digitaler Partikelwelle">
  <h1>Willkommen bei<br>RP-Steuerberatung!</h1>
  <span class="arrow-btn" style="left:67px;top:142px">
    <svg width="11" height="11" viewBox="0 0 12 12"><path d="M11 6H1M5.5 1.5L1 6l4.5 4.5" fill="none" stroke="#111" stroke-width="1.2"/></svg>
  </span>
  <span class="arrow-btn" style="left:660px;top:146px">
    <svg width="11" height="11" viewBox="0 0 12 12"><path d="M1 6h10M6.5 1.5L11 6l-4.5 4.5" fill="none" stroke="#111" stroke-width="1.2"/></svg>
  </span>
  <svg class="band" width="760" height="45" viewBox="0 0 760 45">
    <defs>
      <linearGradient id="bandFill" x1="0" x2="1">
        <stop offset="0" stop-color="#2c4a72"/><stop offset=".4" stop-color="#2b5a98"/><stop offset=".55" stop-color="#1f6fd8"/><stop offset="1" stop-color="#0f4fc8"/>
      </linearGradient>
    </defs>
    <polygon points="0,0 760,31 760,45 0,45" fill="url(#bandFill)"/>
    <polygon points="0,0 760,31 760,34 0,6" fill="#2f7be6"/>
    <rect x="0" y="38" width="300" height="7" fill="#1f2a3d" opacity=".8"/>
  </svg>
</section>

<div class="feature-image" role="img" aria-label="Foto: Berater am Laptop mit eingeblendeten Krypto-Kursdiagrammen"></div>
<p class="intro">Ihrem Spezialisten bei allen steuerlichen Themen rund um Einkünfte &amp; Vermögen aus Krypto-Assets.</p>
<a class="cta">Weiter zu unseren Leistungen
  <svg width="10" height="10" viewBox="0 0 12 12"><path d="M1 6h10M6.5 1.5L11 6l-4.5 4.5" fill="none" stroke="#fff" stroke-width="1.2"/></svg>
</a>

<h2 class="section-title">Quotations:</h2>
<div class="quote" style="top:793px"><span class="num">1</span><p>Dann mach ich eine Schweizer Holding-Gesellschaft– dort zahlt&nbsp; man fast keine Steuern</p></div>
<div class="quote" style="top:873px"><span class="num">2</span><p>Dann melde ich einfach meinen Hauptwohnsitz in Österreich ab</p></div>
<div class="quote" style="top:953px"><span class="num">3</span><p>Dann lass ich meine Kryptos auf einer Börse in Singapur, dort ist das steuerfrei</p></div>

<footer class="footer">
  <div class="brand"><span class="mark"></span>RP STEUERBERATUNG</div>
  <div class="contact">Email: office@rp-steuer.example<br>Phone : +43 512 480 276</div>
  <span class="fnav" style="left:434px">HOME</span>
  <span class="fnav" style="left:476px">LEISTUNGEN</span>
  <span class="fnav" style="left:538px">ÜBER MICH</span>
  <span class="fnav" style="left:594px">KONTAKT</span>
  <span class="fnav" style="left:646px">IMPRESSUM</span>
  <div class="rule"></div>
  <div class="copy">Copyright ©&nbsp; 2022 RP STEUERBERATUNG</div>
</footer>
</body>
</html>
```